School Fairs flyer design

We are running school fairs (Northfield Residential Academies Expo in East Africa) in February 2018. The school fairs and information sessions will take place in Rwanda (February 6th-8th, Kenya February 9th-10th and Uganda on February 11th-12th.)

Rwanda:
Kigali School Fair: February 7th, 1:30-5:30PM
Student Interviews: February 8th, 9:00-1PM
Location: Kigali Lumora Hotel

For information:
Phone number: +250736482915
Email: info@tovaradvisors.example
www.tovarlearningadvisors.example

Features:
*6 US Boarding Schools representative
*Learn about the application process and apply in person.
* Bring your transcripts/school reports to Interview
* www.tovarlearningadvisors.example

Target Market(s)

Students age 11-20 and their parents

Industry/Entity Type

Education

Contact Information for Business Card

Marcel Habarugira
Executive Director
Tovar Consultants
Dallas, Texas
Marcel@tovaradvisers.example
www.tovaradvisors.example
+1614-527-3186

Number of Pages Required

4 page

Font styles to use
Serif

Colors

Designer to choose colors to be used in the design.

Requirements
Must have
• Very clean, elegant and professional designs. Since we offer educational services to students and families, school tours and fairs, as well as institutional support. We would like the designs to reflect what we do.
Nice to have
• Global view, a new logo that incorporates things from our existing logo. We will use this more often but the targeted population is the same.
Should not have
• off colors

```html
<!DOCTYPE html>
<html lang="en">
<head>
<meta charset="utf-8">
<title>Northfield Residential Academies Expo – Flyer</title>
<link href="https://fonts.googleapis.com/css2?family=Lato:wght@400;700;900&family=Raleway:wght@500&display=swap" rel="stylesheet">
<style>
  :root {
    --navy: #2e3192;
    --red: #ed1c24;
    --white: #ffffff;
    --body-grey: #4a4a4a;
    --stage: #e9e9ec;
    --photo-a: #c9b9a4;
    --photo-b: #8aa06b;
    --photo-c: #e4e6ea;
  }
  * { margin: 0; padding: 0; box-sizing: border-box; }
  html, body { width: 978px; height: 1200px; overflow: hidden; background: var(--stage); }
  .stage { position: relative; width: 978px; height: 1200px; }
  .flyer {
    position: absolute; left: 64px; top: 0;
    width: 892px; height: 1260px;
    transform: scale(0.9524); transform-origin: 0 0;
    background: linear-gradient(90deg, #dcdcdc 0%, #ffffff 40%);
    overflow: hidden;
    font-family: 'Lato', sans-serif;
  }
  .shapes { position: absolute; inset: 0; }
  .title {
    position: absolute; right: 40px; top: 55px; text-align: right; line-height: 1;
  }
  .title-lead { display: block; font-weight: 900; font-size: 62px; color: var(--red); letter-spacing: 1px; }
  .title-sub { display: block; font-family: 'Raleway', sans-serif; font-weight: 500; font-size: 40px; color: var(--navy); margin-top: 10px; }
  .title-main { display: block; font-weight: 900; font-size: 108px; color: var(--red); margin-top: 4px; }
  .title-place { display: block; font-family: 'Raleway', sans-serif; font-weight: 500; font-size: 44px; color: var(--navy); margin-top: 10px; }

  .date-badge {
    position: absolute; left: 60px; top: 477px; width: 310px; height: 310px;
    border-radius: 50%; background: var(--white); border: 8px solid var(--red);
    text-align: center;
  }
  .partner-mark { display: flex; align-items: center; justify-content: center; gap: 8px; margin-top: 78px; }
  .partner-dot { width: 18px; height: 18px; border-radius: 50%; background: var(--red); }
  .partner-name { font-weight: 900; font-size: 26px; color: #8b1a1a; }
  .partner-tag { font-size: 13px; color: #666; margin-top: 6px; }
  .badge-rule { width: 240px; height: 1px; background: var(--red); margin: 12px auto 6px; }
  .badge-month { font-weight: 900; font-size: 34px; color: var(--red); line-height: 1.1; }
  .badge-year { font-weight: 900; font-size: 46px; color: var(--red); line-height: 1.05; }

  .schedule { position: absolute; left: 515px; top: 508px; list-style: none; color: var(--white); }
  .schedule li { position: relative; padding-left: 38px; margin-bottom: 12px; }
  .schedule li svg { position: absolute; left: 0; top: 10px; }
  .schedule-country { display: block; font-weight: 900; font-size: 40px; line-height: 1.05; }
  .schedule-dates { display: block; font-weight: 700; font-size: 28px; line-height: 1.2; }

  .features { position: absolute; left: 40px; top: 870px; width: 830px; display: flex; justify-content: space-between; }
  .feature { width: 260px; text-align: center; }
  .feature h2 { font-weight: 700; font-size: 31px; color: var(--navy); margin-bottom: 18px; }
  .feature p { font-size: 13.6px; line-height: 16.2px; color: var(--body-grey); }

  .contact { position: absolute; left: 48px; top: 1150px; color: var(--white); font-size: 20.5px; line-height: 25px; }
  .agency-mark { position: absolute; left: 545px; top: 1160px; display: flex; align-items: center; gap: 12px; }
  .agency-dot { width: 34px; height: 34px; border-radius: 50%; background: var(--navy); }
  .agency-name { font-weight: 900; font-size: 30px; color: var(--navy); }
</style>
</head>
<body>
<div class="stage">
  <article class="flyer">
    <svg class="shapes" viewBox="0 0 892 1260" width="892" height="1260">
      <defs>
        <linearGradient id="photoTone" x1="0" y1="0" x2="1" y2="1">
          <stop offset="0" stop-color="var(--photo-b)"/>
          <stop offset="0.45" stop-color="var(--photo-a)"/>
          <stop offset="1" stop-color="var(--photo-c)"/>
        </linearGradient>
      </defs>
      <polygon points="0,0 892,0 892,432 0,548" fill="url(#photoTone)" role="img" aria-label="Photo of smiling students gathered around a laptop outdoors"/>
      <polygon points="892,430 892,442 0,556 0,544" fill="var(--red)"/>
      <polygon points="0,550 892,438 892,840 0,730" fill="var(--navy)"/>
      <polygon points="0,728 892,838 892,852 0,740" fill="var(--red)"/>
      <polygon points="0,1125 482,1125 412,1260 0,1260" fill="var(--navy)"/>
      <polygon points="500,1088 892,1088 892,1260 412,1260" fill="#f1f1f3"/>
      <polygon points="500,1088 892,1088 892,1096 504,1096 420,1260 410,1260" fill="var(--red)"/>
    </svg>

    <h1 class="title">
      <span class="title-lead">NORTHFIELD</span>
      <span class="title-sub">Residential Academies</span>
      <span class="title-main">EXPO</span>
      <span class="title-place">in East Africa</span>
    </h1>

    <div class="date-badge">
      <div class="partner-mark"><span class="partner-dot"></span><span class="partner-name">GREAT LAKES</span></div>
      <div class="partner-tag">Open Routes</div>
      <div class="badge-rule"></div>
      <div class="badge-month">In February</div>
      <div class="badge-year">2018</div>
    </div>

    <ul class="schedule">
      <li><svg width="20" height="26" viewBox="0 0 20 26"><polyline points="4,3 16,13 4,23" fill="none" stroke="#fff" stroke-width="4"/></svg>
        <span class="schedule-country">RWANDA:</span><span class="schedule-dates">February 6th-8th</span></li>
      <li><svg width="20" height="26" viewBox="0 0 20 26"><polyline points="4,3 16,13 4,23" fill="none" stroke="#fff" stroke-width="4"/></svg>
        <span class="schedule-country">KENYA:</span><span class="schedule-dates">February 9th-10th</span></li>
      <li><svg width="20" height="26" viewBox="0 0 20 26"><polyline points="4,3 16,13 4,23" fill="none" stroke="#fff" stroke-width="4"/></svg>
        <span class="schedule-country">UGANDA:</span><span class="schedule-dates">February 11th-12th</span></li>
    </ul>

    <section class="features">
      <div class="feature"><h2>Lorem Ipsum</h2><p>Lorem ipsum dolor sit amet, consectetuer adipiscing elit, sed diam nonummy nibh euismod tincidunt ut laoreet dolore magna aliquam erat volutpat. Ut wisi enim ad minim veniam, quis nostrud exerci tation ullamcorper suscipit lobortis nisl ut aliquip ex ea commodo consequat.</p></div>
      <div class="feature"><h2>Lorem Ipsum</h2><p>Lorem ipsum dolor sit amet, consectetuer adipiscing elit, sed diam nonummy nibh euismod tincidunt ut laoreet dolore magna aliquam erat volutpat. Ut wisi enim ad minim veniam, quis nostrud exerci tation ullamcorper suscipit lobortis nisl ut aliquip ex ea commodo consequat.</p></div>
      <div class="feature"><h2>Lorem Ipsum</h2><p>Lorem ipsum dolor sit amet, consectetuer adipiscing elit, sed diam nonummy nibh euismod tincidunt ut laoreet dolore magna aliquam erat volutpat. Ut wisi enim ad minim veniam, quis nostrud exerci tation ullamcorper suscipit lobortis nisl ut aliquip ex ea commodo consequat.</p></div>
    </section>

    <address class="contact" style="font-style:normal">
      Address: pleae enter your text here<br>
      Ph: 000 0000 0000<br>
      E: youremail@example.com
    </address>

    <div class="agency-mark"><span class="agency-dot"></span><span class="agency-name">Tovar Consultants</span></div>
  </article>
</div>
</body>
</html>
```